Modernization of our corporate website

The goal of this task is to propose a new template for our website, http://vlomik.example/

We just made a new batch of business cards (see attachments) and the new website has to match them.

Feel free to request current HTML.

Industry/Entity Type

Business

```html
<!DOCTYPE html>
<html lang="fr">
<head>
<meta charset="utf-8">
<title>vlomik . Hosting Architects — Contact</title>
<link rel="stylesheet" href="https://fonts.googleapis.com/css2?family=Carlito:wght@400;700&display=swap">
<style>
:root{
  --bg:#efefef;
  --bg-light:#fbfbfb;
  --ink:#111;
  --muted:#8a8a8a;
  --rule:#c4c4c4;
  --nav-1:#3a3aa0;
  --nav-2:#b02a4a;
  --nav-3:#d62ad6;
  --nav-4:#27d6e0;
  --nav-5:#29e02a;
  --accent:#3cf01a;
  --foot-1:#e6e61e;
  --foot-2:#8b8be0;
  --map-base:#e6e0d2;
  --map-road:#f4e27a;
}
*{margin:0;padding:0;box-sizing:border-box}
html,body{width:1200px;height:833px;overflow:hidden}
body{
  position:relative;
  font-family:"Carlito",Calibri,sans-serif;
  color:var(--ink);
  background:
    radial-gradient(ellipse 420px 520px at 230px 200px,var(--bg-light),transparent 70%),
    linear-gradient(180deg,#f3f3f3 0%,var(--bg) 100%);
}
.backdrop{position:absolute;inset:0;pointer-events:none}
.site-title{
  position:absolute;top:56px;left:0;width:1200px;text-align:center;
  font-size:46px;font-weight:400;letter-spacing:.2px;
}
.main-nav{
  position:absolute;top:112px;left:0;width:1200px;text-align:center;
  font-size:19px;color:#222;
}
.main-nav span{border-left:2px solid;padding-left:7px;margin-left:5px}
.main-nav .n1{border-color:var(--nav-1)}
.main-nav .n2{border-color:var(--nav-2)}
.main-nav .n3{border-color:var(--nav-3)}
.main-nav .n4{border-color:var(--nav-4)}
.main-nav .n5{border-color:var(--nav-5)}
.page-title{
  position:absolute;top:209px;left:491px;
  font-size:56px;font-weight:400;line-height:60px;
}
.page-title::before{
  content:"";position:absolute;left:0;top:4px;width:9px;height:50px;background:var(--accent);
}
.page-title span{padding-left:11px}
.contact-details{
  position:absolute;top:378px;left:126px;
  font-size:19px;line-height:44px;color:#1a1a1a;list-style:none;
}
.location-map{
  position:absolute;top:348px;left:640px;width:425px;height:259px;
}
.footer-nav{
  position:absolute;top:688px;left:0;width:1200px;text-align:center;
  font-size:17px;font-weight:700;color:#6d6d6d;
}
.footer-nav span{border-left:2px solid;padding-left:6px;margin-left:4px}
.footer-nav .f1{border-color:var(--foot-1)}
.footer-nav .f2{border-color:var(--foot-2)}
.footer-nav .f3{border-color:var(--accent);font-weight:400}
.footer-rule{
  position:absolute;top:731px;left:126px;width:935px;height:3px;background:var(--rule);
}
.legal{
  position:absolute;top:741px;left:0;width:1165px;text-align:center;
  font-size:14px;line-height:15px;color:var(--muted);
}
.social{
  position:absolute;top:754px;left:985px;display:flex;align-items:center;gap:6px;
  font-size:16px;color:#b5b5b5;
}
.social i{display:block;width:14px;height:14px;border-radius:50%;background:#c9c9c9}
</style>
</head>
<body>
<svg class="backdrop" width="1200" height="833" aria-hidden="true">
  <path d="M560 0 C760 20 830 180 760 330 L1200 330 L1200 0 Z" fill="#f0f0f0"/>
  <path d="M760 0 C820 60 830 160 780 260" fill="none" stroke="#ffffff" stroke-width="3" opacity=".8"/>
</svg>

<h1 class="site-title">vlomik . Hosting Architects</h1>
<nav class="main-nav">
  <span class="n1">accueil</span>
  <span class="n2">Hebergement</span>
  <span class="n3">ERP on a drive</span>
  <span class="n4">Nano CDN</span>
  <span class="n5">Etudes de cas</span>
</nav>

<h2 class="page-title"><span>Contact</span></h2>

<ul class="contact-details">
  <li>Pour toute demande commerciale : contact (@) vlomik.example</li>
  <li>Pour toute demande technique : support (@) vlomik.example</li>
  <li>Courrier :</li>
  <li>VLOMIK</li>
  <li>14 rue des Tilleuls</li>
  <li>75011 PARIS</li>
</ul>

<div class="location-map" role="img" aria-label="Plan de situation du bureau dans le quartier"
     style="background:linear-gradient(135deg,var(--map-base) 0%,#ece5c8 50%,var(--map-base) 100%)"></div>

<nav class="footer-nav">
  <span class="f1">L'infrastructure</span>
  <span class="f2">La société</span>
  <span class="f3">Contact</span>
</nav>
<div class="footer-rule"></div>
<p class="legal">14 rue des Tilleuls - 75011 Paris - France<br>RCS Paris B 512 384 906 (00024)</p>
<div class="social"><i></i>vlomik</div>
</body>
</html>
```